Business cards for a high-end menswear store

I would like to come up with a design for our business cards.
Two different ones: one for general sales and one for the owner. It is a high-end menswear store.

Our address is: 4817 Morneau Boulevard, Montreal, QC, K7P4M2
phone number: 514-286-5937
insta: MAISONVERLAINE
Website: www.maisonverlaine.example
email (general card): info@maisonverlaine.example
email (owner): bastien@maisonverlaine.example

I have attached our logo in an ai and eps file format. You can see our old cards as well. I am looking for a modern and clean look.

Target Market(s)

High-End Clothing Market

Industry/Entity Type

Retail, Clothing, Luxury Clothing

Contact Information for Business Card

Address, Name, Email, Website, Social Info,

Font styles to use
Serif

Colors

Designer to choose colors to be used in the design.

Requirements
Must have
• Address, Name, Email, Website, Social Info,
Nice to have
• QR Code that brings you to the website

```html
<!DOCTYPE html>
<html lang="en">
<head>
<meta charset="utf-8">
<title>Maison Verlaine — Business Cards</title>
<link rel="stylesheet" href="https://fonts.googleapis.com/css2?family=Montserrat:wght@400;500&display=swap">
<style>
  :root {
    --backdrop: #2b2b2b;
    --card: #1f1d1d;
    --card-edge: #141313;
    --ink: #f4f4f4;
    --ink-soft: #d9d9d9;
  }
  * { margin: 0; padding: 0; box-sizing: border-box; }
  html, body {
    width: 1200px; height: 960px; overflow: hidden;
    background: var(--backdrop);
    font-family: "Montserrat", sans-serif;
    color: var(--ink);
  }
  .sheet {
    position: relative; width: 1200px; height: 960px;
  }
  .card {
    position: absolute; left: 240px;
    width: 720px; height: 412px;
    background: var(--card);
    border-radius: 28px;
    box-shadow: 0 4px 0 var(--card-edge), 0 18px 40px rgba(0,0,0,.45);
  }
  .card--front { top: 48px; }
  .card--back  { top: 500px; }

  .wordmark {
    font-weight: 400;
    letter-spacing: 0.32em;
    text-transform: uppercase;
    color: var(--ink);
    line-height: 1.2;
  }
  .card--front .wordmark {
    position: absolute; inset: 0;
    display: flex; align-items: center; justify-content: center;
    font-size: 40px;
    padding-left: 0.32em;
  }
  .card--back .wordmark {
    position: absolute; left: 52px; top: 48px;
    font-size: 26px;
  }

  .social {
    position: absolute; right: 56px; top: 52px;
    display: flex; align-items: center; gap: 10px;
    font-size: 17px; font-weight: 400; letter-spacing: 0.02em;
  }
  .social__dot {
    width: 16px; height: 16px; border-radius: 50%;
    background: var(--ink);
  }

  .contact-list {
    position: absolute; left: 52px; bottom: 40px;
    list-style: none;
    display: flex; flex-direction: column; gap: 7px;
    font-size: 19px;
  }
  .contact-list li { display: flex; align-items: center; gap: 14px; }
  .contact-list svg { width: 20px; height: 20px; flex: none; }

  .address {
    position: absolute; right: 56px; top: 196px;
    display: flex; align-items: flex-start; gap: 14px;
    font-size: 19px; line-height: 1.4;
  }
  .address svg { width: 20px; height: 26px; margin-top: 10px; flex: none; }
</style>
</head>
<body>
<main class="sheet">

  <section class="card card--front" aria-label="Card front">
    <div class="wordmark">Maison Verlaine</div>
  </section>

  <section class="card card--back" aria-label="Card back">
    <div class="wordmark">Maison Verlaine</div>

    <div class="social">
      <span class="social__dot"></span>
      <span>MAISONVERLAINE</span>
    </div>

    <div class="address">
      <svg viewBox="0 0 20 26" aria-hidden="true">
        <path d="M10 0C4.5 0 0 4.4 0 9.8 0 16.8 10 26 10 26s10-9.2 10-16.2C20 4.4 15.5 0 10 0z" fill="#f4f4f4"/>
        <circle cx="10" cy="9.6" r="3.6" fill="#1f1d1d"/>
      </svg>
      <div>
        4817 Morneau Boulevard<br>
        Montreal, QC, K7P4M2
      </div>
    </div>

    <ul class="contact-list">
      <li>
        <svg viewBox="0 0 20 20" aria-hidden="true">
          <path d="M4.2 1.5l3 3.3-1.6 2.3c1 2.3 2.8 4.1 5.1 5.1l2.3-1.6 3.3 3-1.7 3.2C8.3 16.6 3.4 11.7 1 5z" fill="#f4f4f4"/>
        </svg>
        <span>514-286-5937</span>
      </li>
      <li>
        <svg viewBox="0 0 20 20" aria-hidden="true">
          <rect x="1" y="4" width="18" height="12" rx="1.5" fill="#f4f4f4"/>
          <path d="M1.8 5l8.2 6.2L18.2 5" fill="none" stroke="#1f1d1d" stroke-width="1.6"/>
        </svg>
        <span>info@maisonverlaine.example</span>
      </li>
      <li>
        <svg viewBox="0 0 20 20" aria-hidden="true">
          <rect x="1" y="4" width="18" height="12" rx="1.5" fill="#f4f4f4"/>
          <path d="M1.8 5l8.2 6.2L18.2 5" fill="none" stroke="#1f1d1d" stroke-width="1.6"/>
        </svg>
        <span>bastien@maisonverlaine.example</span>
      </li>
      <li>
        <svg viewBox="0 0 20 20" aria-hidden="true">
          <circle cx="10" cy="10" r="9" fill="#f4f4f4"/>
          <ellipse cx="10" cy="10" rx="4" ry="9" fill="none" stroke="#1f1d1d" stroke-width="1.4"/>
          <path d="M1 10h18" stroke="#1f1d1d" stroke-width="1.4"/>
        </svg>
        <span>www.maisonverlaine.example</span>
      </li>
    </ul>
  </section>

</main>
</body>
</html>
```